RONEK PIPE SYSTEMS

Wrap designed for truck using ronek pipe logo colours, have yellow, blue, green water drops and hydraulics hoses. More colour.

Requirements
Must have
• Wrap designed for truck using ronek pipe logo colours, have yellow, blue, green water drops and hydraulics hoses. More colour.
Nice to have

```html
<!DOCTYPE html>
<html lang="en">
<head>
<meta charset="utf-8">
<title>Ronek Pipe Systems – Truck Wrap</title>
<link rel="stylesheet" href="https://fonts.googleapis.com/css2?family=Archivo+Black&family=Montserrat:wght@500;700;800&display=swap">
<style>
  :root {
    --navy: #1c2a8c;
    --royal: #1f45c4;
    --sky: #1b66d6;
    --deep: #142079;
    --green: #2f9a4a;
    --lime: #8cc63f;
    --paper: #f1f1f1;
    --bg: #f7f7f7;
    --hose: #c9c9c9;
  }
  html, body { margin: 0; padding: 0; overflow: hidden; background: var(--bg); }
  .canvas { width: 1200px; height: 2595px; display: block; }
  .brand-name { font-family: "Archivo Black", sans-serif; fill: var(--navy); }
  .tagline { font-family: "Montserrat", sans-serif; font-weight: 800; fill: var(--navy); letter-spacing: .5px; }
  .service { font-family: "Montserrat", sans-serif; font-weight: 500; fill: var(--navy); font-variant: small-caps; letter-spacing: .5px; }
  .web { font-family: "Montserrat", sans-serif; font-weight: 500; fill: #fff; letter-spacing: 1.5px; }
  .phone { font-family: "Montserrat", sans-serif; font-weight: 500; fill: var(--navy); }
  .panel { fill: var(--paper); }
</style>
</head>
<body>
<svg class="canvas" viewBox="0 0 1200 2595" xmlns="http://www.w3.org/2000/svg">
  <defs>
    <linearGradient id="sweep" x1="0" y1="0" x2="1" y2="1">
      <stop offset="0" stop-color="var(--sky)"/>
      <stop offset="1" stop-color="var(--deep)"/>
    </linearGradient>
    <linearGradient id="swoosh" x1="0" y1="0" x2="1" y2="0">
      <stop offset="0" stop-color="var(--green)"/>
      <stop offset="1" stop-color="var(--lime)"/>
    </linearGradient>
    <linearGradient id="hoses" x1="0" y1="0" x2="1" y2="0">
      <stop offset="0" stop-color="var(--hose)" stop-opacity=".15"/>
      <stop offset=".5" stop-color="var(--hose)" stop-opacity=".5"/>
      <stop offset="1" stop-color="var(--hose)" stop-opacity=".15"/>
    </linearGradient>
  </defs>

  <!-- Front box panel -->
  <g class="front-box">
    <rect class="panel" x="420" y="80" width="332" height="150" rx="8"/>
    <text class="brand-name" x="586" y="172" font-size="52" text-anchor="middle">RONEK</text>
    <text class="brand-name" x="586" y="196" font-size="20" text-anchor="middle">PIPE SYSTEMS</text>
    <text class="tagline" x="586" y="212" font-size="10" text-anchor="middle">FUEL · AIR · WATER · OIL · GREASE</text>
  </g>

  <!-- Front cab nose band -->
  <g class="front-cab">
    <path d="M460,395 L692,395 L692,465 L460,465 Z" fill="url(#sweep)"/>
    <path d="M468,400 C520,445 600,462 690,463 L690,455 C600,452 530,438 468,400 Z" fill="url(#swoosh)"/>
    <path d="M475,398 C525,440 600,455 690,456 L690,465 L460,465 Z" fill="var(--paper)" opacity=".0"/>
  </g>

  <!-- Driver side box -->
  <g class="side-left-box">
    <rect class="panel" x="352" y="752" width="758" height="316"/>
    <rect x="640" y="765" width="260" height="290" fill="url(#hoses)" role="img" aria-label="Faint hydraulic hoses and fittings"/>
    <path d="M965,752 C930,900 800,1010 590,1068 L1110,1068 L1110,752 Z" fill="url(#sweep)" role="img" aria-label="Blue sweep with gear pattern"/>
    <path d="M930,872 C870,985 750,1045 560,1066 L610,1066 C770,1040 880,985 930,872 Z" fill="url(#swoosh)"/>
    <text class="brand-name" x="540" y="950" font-size="86" text-anchor="middle">RONEK</text>
    <text class="brand-name" x="540" y="982" font-size="29" text-anchor="middle">PIPE SYSTEMS</text>
    <text class="tagline" x="540" y="1002" font-size="14" text-anchor="middle">FUEL · AIR · WATER · OIL · GREASE</text>
    <text class="service" x="540" y="1025" font-size="17" text-anchor="middle">Complete House &amp; Fitting Supply</text>
  </g>

  <!-- Driver side cab -->
  <g class="side-left-cab">
    <path d="M92,885 L300,885 L300,1135 L92,1135 Z" class="panel"/>
    <path d="M258,885 L300,885 L300,1135 L110,1135 C190,1090 250,1030 258,885 Z" fill="url(#sweep)"/>
    <path d="M240,1010 C210,1070 160,1110 92,1130 L92,1122 C155,1102 205,1065 240,1010 Z" fill="url(#swoosh)"/>
    <text class="brand-name" x="148" y="1057" font-size="18" text-anchor="middle">RONEK</text>
    <text class="tagline" x="148" y="1066" font-size="5" text-anchor="middle">PIPE SYSTEMS</text>
  </g>

  <!-- Rear doors -->
  <g class="rear">
    <rect class="panel" x="418" y="1380" width="320" height="365"/>
    <rect x="620" y="1400" width="110" height="230" fill="url(#hoses)" role="img" aria-label="Faint hydraulic hoses and fittings"/>
    <path d="M418,1520 C470,1620 600,1660 738,1660 L738,1745 L418,1745 Z" fill="url(#sweep)" role="img" aria-label="Blue sweep with gear pattern"/>
    <path d="M470,1585 C540,1635 620,1652 738,1652 L738,1664 C620,1664 535,1645 470,1585 Z" fill="url(#swoosh)"/>
    <text class="brand-name" x="584" y="1532" font-size="56" text-anchor="middle">RONEK</text>
    <text class="brand-name" x="584" y="1556" font-size="21" text-anchor="middle">PIPE SYSTEMS</text>
    <text class="tagline" x="584" y="1573" font-size="11" text-anchor="middle">FUEL · AIR · WATER · OIL · GREASE</text>
    <text class="service" x="584" y="1597" font-size="19" text-anchor="middle">Service Queensland</text>
    <text class="web" x="584" y="1708" font-size="14" text-anchor="middle">RONEKPIPE.COM.AU</text>
    <path d="M450,1745 L472,1722 L738,1722 L738,1745 Z" fill="#fff"/>
    <text class="phone" x="590" y="1738" font-size="12" text-anchor="middle">✆ 0400 123 456 | ✆ 0400 765 432</text>
  </g>

  <!-- Passenger side box -->
  <g class="side-right-box">
    <rect class="panel" x="80" y="2040" width="778" height="325"/>
    <rect x="270" y="2050" width="260" height="290" fill="url(#hoses)" role="img" aria-label="Faint hydraulic hoses and fittings"/>
    <path d="M80,2040 L225,2040 C250,2200 380,2320 540,2365 L80,2365 Z" fill="url(#sweep)" role="img" aria-label="Blue sweep with gear pattern"/>
    <path d="M268,2160 C320,2270 440,2340 620,2362 L570,2362 C420,2340 310,2270 268,2160 Z" fill="url(#swoosh)"/>
    <text class="brand-name" x="650" y="2240" font-size="86" text-anchor="middle">RONEK</text>
    <text class="brand-name" x="650" y="2272" font-size="29" text-anchor="middle">PIPE SYSTEMS</text>
    <text class="tagline" x="650" y="2292" font-size="14" text-anchor="middle">FUEL · AIR · WATER · OIL · GREASE</text>
    <text class="service" x="650" y="2315" font-size="17" text-anchor="middle">Complete House &amp; Fitting Supply</text>
  </g>

  <!-- Passenger side cab -->
  <g class="side-right-cab">
    <path d="M888,2172 L1110,2172 L1110,2440 L888,2440 Z" class="panel"/>
    <path d="M888,2172 L935,2172 C945,2320 1010,2400 1100,2440 L888,2440 Z" fill="url(#sweep)"/>
    <path d="M960,2300 C990,2370 1040,2410 1110,2430 L1110,2440 C1035,2420 980,2375 960,2300 Z" fill="url(#swoosh)"/>
    <text class="brand-name" x="1043" y="2345" font-size="18" text-anchor="middle">RONEK</text>
    <text class="tagline" x="1043" y="2354" font-size="5" text-anchor="middle">PIPE SYSTEMS</text>
  </g>
</svg>
</body>
</html>
```